Thank You Card

I'm looking for a thank you card design using our logo and other graphics. We are an essential business and our employees (Electricians) have done an incredible job staying healthy and safe during the COVID-19 pandemic, I want to send each a thank you card.

```html
<!DOCTYPE html>
<html lang="en">
<head>
<meta charset="utf-8">
<title>Thank You Card – Brightline Service Co.</title>
<link rel="stylesheet" href="https://fonts.googleapis.com/css2?family=Montserrat:wght@300;400;500;600;800;900&family=Great+Vibes&display=swap">
<style>
  :root {
    --stage: #e9e9ec;
    --frame-blue: #0a2bb8;
    --frame-deep: #041a8a;
    --paper: #ffffff;
    --brand-red: #ec0a1c;
    --brand-navy: #14298f;
    --ink: #111111;
    --silk-light: #fbfbfb;
    --silk-shade: #d9d9d9;
  }
  * { margin: 0; padding: 0; box-sizing: border-box; }
  html, body { width: 1200px; height: 1022px; overflow: hidden; }
  body {
    background: var(--stage);
    font-family: "Montserrat", Arial, sans-serif;
    position: relative;
  }
  .spread {
    position: absolute;
    left: 81px;
    width: 1038px;
    height: 371px;
    background: linear-gradient(135deg, var(--frame-blue) 0%, var(--frame-deep) 50%, var(--frame-blue) 100%);
  }
  .spread--cover { top: 94px; }
  .spread--inside { top: 561px; }
  .spread::after {
    content: "";
    position: absolute;
    left: 508px; top: 0;
    width: 24px; height: 100%;
    background: linear-gradient(90deg, var(--frame-blue), var(--frame-deep) 50%, var(--frame-blue));
  }
  .panel {
    position: absolute;
    top: 11px;
    width: 497px;
    height: 349px;
    background: var(--paper);
    overflow: hidden;
  }
  .panel--left { left: 11px; }
  .panel--right { left: 530px; }
  .panel::after {
    content: "";
    position: absolute;
    inset: 4px;
    border: 1px solid var(--brand-red);
    pointer-events: none;
  }
  .silk {
    position: absolute;
    inset: 0;
    background:
      radial-gradient(ellipse 70% 30% at 30% 30%, var(--silk-shade), transparent 70%),
      radial-gradient(ellipse 80% 25% at 70% 70%, var(--silk-shade), transparent 70%),
      linear-gradient(160deg, var(--silk-light) 0%, #eeeeee 45%, var(--silk-light) 70%, #e6e6e6 100%);
  }
  .centered {
    position: absolute;
    left: 0; right: 0;
    text-align: center;
    transform: translateY(-50%);
  }
  .brand-name {
    color: var(--brand-red);
    font-weight: 800;
    text-transform: uppercase;
    line-height: 1.05;
    letter-spacing: 0.5px;
  }
  .brand-name--small { font-size: 17px; }
  .brand-name--large { font-size: 26px; }
  .web-address {
    color: var(--brand-navy);
    font-size: 13px;
    font-weight: 400;
  }
  .thank-you {
    position: absolute;
    left: 46px;
    top: 130px;
  }
  .thank-you text {
    fill: var(--brand-red);
    font-family: "Great Vibes", cursive;
  }
  .occasion {
    color: var(--brand-navy);
    font-size: 14px;
    font-weight: 600;
  }
  .hero-headline {
    position: absolute;
    left: 79px;
    top: 92px;
  }
  .hero-headline text { font-family: "Montserrat", Arial, sans-serif; font-weight: 900; }
  .hero-headline .line-navy { fill: var(--brand-navy); }
  .hero-headline .line-red { fill: var(--brand-red); }
  .message-lead {
    font-size: 20.5px;
    font-weight: 300;
    color: var(--brand-navy);
    line-height: 1.4;
  }
  .message-body {
    font-size: 14px;
    font-weight: 400;
    color: var(--brand-navy);
    line-height: 1.45;
  }
  .accent { color: var(--brand-red); }
  .sign-off { font-size: 14px; color: var(--brand-red); }
  .signature { font-size: 14px; font-weight: 500; color: var(--ink); }
</style>
</head>
<body>

  <section class="spread spread--cover">
    <article class="panel panel--left back-cover">
      <div class="silk" role="img" aria-label="Soft white silk fabric background"></div>
      <div class="centered brand-name brand-name--small" style="top:174px;">Brightline<br>Service Co.</div>
      <div class="centered web-address" style="top:313px;">www.BrightlineService.com</div>
    </article>
    <article class="panel panel--right front-cover">
      <div class="silk" role="img" aria-label="Soft white silk fabric background"></div>
      <div class="centered brand-name brand-name--large" style="top:72px;">Brightline<br>Service Co.</div>
      <svg class="thank-you" width="405" height="140" viewBox="0 0 405 140" aria-label="Thank You">
        <text x="0" y="100" font-size="100" textLength="400" lengthAdjust="spacingAndGlyphs">Thank You</text>
      </svg>
      <div class="centered occasion" style="top:312px;">Essential Worker 2020</div>
    </article>
  </section>

  <section class="spread spread--inside">
    <article class="panel panel--left inside-left">
      <svg class="hero-headline" width="340" height="160" viewBox="0 0 340 160" aria-label="You're a hero">
        <text class="line-navy" x="0" y="55" font-size="70" textLength="340" lengthAdjust="spacingAndGlyphs">YOU’RE A</text>
        <text class="line-red" x="0" y="156" font-size="112" textLength="340" lengthAdjust="spacingAndGlyphs">HERO</text>
      </svg>
    </article>
    <article class="panel panel--right inside-right">
      <div class="centered message-lead" style="top:86px;">
        You have done an<br>
        incredible job providing essential services<br>
        <span class="accent">during the COVID-19 pandemic.</span>
      </div>
      <div class="centered message-body" style="top:181px;">
        <span class="accent">Stay safe and healthy,</span> if there is anything I can do for you<br>
        please let me know.
      </div>
      <div class="centered sign-off" style="top:250px;">With gratitude,</div>
      <div class="centered signature" style="top:292px;">Daniel Harper</div>
    </article>
  </section>

</body>
</html>
```